Bierlogo gesucht
Zielgruppe
Bierherstellung / Zielgruppe sowohl Konsumenten von traditionellen Sorten als auch Liebhaber von Craftbeer
Aufgabenstellung
Aufgabe ist die Gestaltung eines Bieretiketts für den Brustbereich der Flasche / Weitere Auftragserweiterung Website und Cooperate Identity gewünscht / Lebensmittelrechtlich relevante Angaben sind zu berücksichtigen / Herstellung im Raum Oberbayern - Ammersee
Logo in Verbindung mit dem Namen "Haldbrunner" soll sowohl Qualität als auch Offenheit für neue Einflüsse, Rezepte, Inhaltsstoffe vermitteln, Stil kann gerne sehr einfach bzgl. Farbgebung aber einprägsam sein

```html
<!DOCTYPE html>
<html lang="de">
<head>
<meta charset="utf-8">
<title>Haldbrunner Bier – Etikett</title>
<link rel="stylesheet" href="https://fonts.googleapis.com/css2?family=Rye&family=Oswald:wght@600&family=Open+Sans+Condensed:wght@300;700&family=Open+Sans:wght@400;700&display=swap">
<style>
  :root {
    --paper: #fdfdfd;
    --oval-black: #0b0a09;
    --ring-green: #1b6a16;
    --field-warm: #3a230f;
    --field-dark: #0f0b08;
    --band-green: #156007;
    --band-red: #7a0000;
    --gold: #ebbd6d;
    --white: #ffffff;
    --art-light: #c9a266;
    --art-dark: #7a4a16;
  }
  html, body {
    margin: 0;
    width: 1200px;
    height: 726px;
    overflow: hidden;
    background: var(--paper);
  }
  .canvas { display: block; width: 1200px; height: 726px; }
  .label--green { --band: var(--band-green); }
  .label--red { --band: var(--band-red); }
  .oval-outer { fill: var(--oval-black); }
  .oval-ring { fill: none; stroke: var(--ring-green); stroke-width: 3.5; }
  .band, .band-stripe, .band-tab { fill: var(--band); }
  .band-gap { fill: var(--white); }
  .wordmark {
    font-family: "Rye", serif;
    fill: var(--white);
    text-anchor: middle;
  }
  .subline {
    font-family: "Oswald", sans-serif;
    font-weight: 600;
    fill: var(--gold);
    text-anchor: middle;
  }
  .craft {
    font-family: "Rye", serif;
    fill: var(--gold);
    text-anchor: middle;
  }
  .facts {
    font-family: "Open Sans", sans-serif;
    fill: var(--white);
    text-anchor: end;
    font-size: 7px;
  }
  .facts__head, .facts__volume { font-weight: 700; }
  .facts__volume { font-size: 8.5px; }
</style>
</head>
<body>
<svg class="canvas" viewBox="0 0 1200 726" xmlns="http://www.w3.org/2000/svg">
  <defs>
    <radialGradient id="field" cx="50%" cy="55%" r="55%">
      <stop offset="0" stop-color="var(--field-warm)"/>
      <stop offset="1" stop-color="var(--field-dark)"/>
    </radialGradient>
    <linearGradient id="artwork" x1="0" y1="0" x2="0" y2="1">
      <stop offset="0" stop-color="var(--art-light)"/>
      <stop offset="1" stop-color="var(--art-dark)"/>
    </linearGradient>

    <g id="label">
      <!-- oval -->
      <ellipse class="oval-outer" cx="313" cy="355" rx="213" ry="305"/>
      <ellipse cx="313" cy="355" rx="199" ry="291" fill="url(#field)"/>
      <ellipse class="oval-ring" cx="313" cy="355" rx="201" ry="293"/>

      <!-- brewing artwork area -->
      <g role="img" aria-label="Illustration: Holzfass mit Braugeräten, Schaufel, Maischgabel und Gerstenähren">
        <rect x="228" y="84" width="170" height="170" rx="18" fill="url(#artwork)" opacity="0.85"/>
      </g>

      <!-- band -->
      <polygon class="band-gap" points="48,275 576,139 576,431 48,567"/>
      <polygon class="band-stripe" points="48,275 576,139 576,143 48,279"/>
      <polygon class="band-stripe" points="48,563 576,427 576,431 48,567"/>
      <circle class="band-tab" cx="48" cy="421" r="28"/>
      <circle class="band-tab" cx="576" cy="282" r="28"/>
      <polygon class="band" points="48,287 576,151 576,419 48,555"/>

      <!-- wordmark -->
      <text class="wordmark" font-size="62" x="338" y="292" textLength="340" lengthAdjust="spacingAndGlyphs" transform="rotate(-14.5 338 292)">HALDBRUNNER</text>
      <text class="wordmark" font-size="160" x="258" y="462" textLength="318" lengthAdjust="spacingAndGlyphs" transform="rotate(-14.5 258 462)">BIER</text>

      <!-- ingredients -->
      <text class="facts" x="570">
        <tspan class="facts__head" x="570" y="340">ZUTATEN:</tspan>
        <tspan x="570" y="350">Wasser, Gerstenmalz, Hopfen, Hefe</tspan>
        <tspan x="570" y="360">D-86911 Seewald</tspan>
        <tspan x="570" y="370">Alk. 4,9% vol.</tspan>
        <tspan class="facts__volume" x="570" y="390">℮ 50 cl</tspan>
      </text>

      <!-- sub lines -->
      <text class="subline" font-size="36" x="335" y="535" textLength="290" lengthAdjust="spacingAndGlyphs" transform="rotate(-21 335 535)">BIERSPEZIALITÄTEN</text>
      <text class="craft" font-size="30" x="313" y="618" textLength="135" lengthAdjust="spacingAndGlyphs" transform="rotate(-15 313 618)">Craftbeer</text>
    </g>
  </defs>

  <use class="label--green" href="#label"/>
  <use class="label--red" href="#label" transform="translate(580 9)"/>
</svg>
</body>
</html>
```